Medical IT Business with New logo needs a fresh stationary design

First time on sketch Harbor; Thought I would give it a go.
This project is for business cards alone but we have loads of design work that needs to take place in the immediate future.

We provide IT services to the Medical Industry and value ourselves as offering a premium product to the market.

I am after a fresh, clean design using full colour 2 sided cards which includes our current colour palettes from our logo.

Card's must include:
- Logo
- Slogan
- Name
- Adress
- Email
- Phone
- Fax
- Mobile

Target Market(s)

Surgeons, High Profile Medical Personnel

Industry/Entity Type

Business

Fonts, CMYK Colours and Logo files attached.

Requirements
Must have
• Card's must include:
• - Logo
• - Slogan
• - Name
• - Adress
• - Email
• - Phone
• - Fax
• - Mobile
Nice to have
• Needs to incorporate our colour palette (attached CMYK colours)
Should not have
• Black backgrounds. Black text ok.

```html
<!DOCTYPE html>
<html lang="en">
<head>
<meta charset="utf-8">
<title>Clinivo Systems – Business Card</title>
<link rel="stylesheet" href="https://fonts.googleapis.com/css2?family=Open+Sans:wght@400;600;700;800&display=swap">
<style>
  :root{
    --navy:#1d3f6f;
    --navy-deep:#15325c;
    --blue:#2a7fb8;
    --sky:#3d9fd3;
    --text:#3e4650;
    --muted:#7a8fa3;
    --paper:#ffffff;
    --paper-shade:#e9ecef;
    --backdrop:#eef0f2;
  }
  *{box-sizing:border-box;margin:0;padding:0}
  html,body{width:1200px;height:843px;overflow:hidden;background:var(--backdrop);font-family:"Open Sans",sans-serif}
  .stage{position:relative;width:1200px;height:843px}
  .card{position:absolute;top:273px;width:520px;height:297px;overflow:hidden;box-shadow:0 6px 18px rgba(0,0,0,.18)}
  /* back side */
  .card-back{left:50px;background:linear-gradient(100deg,var(--blue) 0%,var(--navy) 60%,var(--navy-deep) 100%)}
  .card-back .disc{position:absolute;left:-60px;top:-70px;width:360px;height:360px;border-radius:50%;background:var(--sky);opacity:.55}
  .card-back .brand{position:absolute;left:290px;top:108px;color:#fff;font-weight:700;font-size:30px;line-height:1.02;letter-spacing:.5px}
  .card-back .tagline{position:absolute;left:292px;top:174px;color:#fff;font-size:11px;letter-spacing:.3px}
  .card-back .web{position:absolute;left:292px;top:192px;color:#fff;font-size:14px;letter-spacing:.5px}
  /* front side */
  .card-front{left:630px;background:linear-gradient(160deg,var(--paper) 40%,var(--paper-shade) 100%)}
  .logo{position:absolute;left:30px;top:24px;display:flex;align-items:center;gap:10px}
  .logo .dot{width:44px;height:44px;border-radius:50%;background:var(--blue)}
  .logo .name{color:var(--navy);font-weight:700;font-size:24px;line-height:1;letter-spacing:.3px}
  .slogan{position:absolute;left:85px;top:76px;color:var(--sky);font-size:10.5px}
  .address{position:absolute;left:32px;top:108px;color:var(--text);font-size:12.5px;line-height:1.35}
  .contacts{position:absolute;left:32px;top:148px;list-style:none;color:var(--text);font-size:12.5px;line-height:20px}
  .contacts li{display:flex;align-items:center;gap:8px}
  .contacts svg{width:12px;height:12px;fill:var(--navy)}
  .person{position:absolute;right:58px;top:212px;text-align:right}
  .person .who{color:var(--navy);font-weight:700;font-size:16px;letter-spacing:.3px}
  .person .role{color:var(--blue);font-size:12.5px}
  .tab{position:absolute;right:0;top:218px;width:10px;height:34px;background:var(--blue)}
</style>
</head>
<body>
<main class="stage">
  <section class="card card-back" aria-label="Card back">
    <div class="disc"></div>
    <div class="brand">CLINIVO<br>SYSTEMS</div>
    <div class="tagline">always beside your clinic</div>
    <div class="web">www.clinivo.com</div>
  </section>

  <section class="card card-front" aria-label="Card front">
    <div class="logo"><span class="dot"></span><span class="name">CLINIVO<br>SYSTEMS</span></div>
    <div class="slogan">always beside your clinic</div>
    <div class="address">4120 Larkspur Road<br>Juneau, Alaska 99801</div>
    <ul class="contacts">
      <li><svg viewBox="0 0 24 24"><path d="M6.6 10.8a15 15 0 0 0 6.6 6.6l2.2-2.2c.3-.3.7-.4 1-.2 1.1.4 2.3.6 3.6.6.6 0 1 .4 1 1V20c0 .6-.4 1-1 1A17 17 0 0 1 3 4c0-.6.4-1 1-1h3.5c.6 0 1 .4 1 1 0 1.3.2 2.5.6 3.6.1.3 0 .7-.2 1z"/></svg>555 214 7730</li>
      <li><svg viewBox="0 0 24 24"><path d="M7 1h10a2 2 0 0 1 2 2v18a2 2 0 0 1-2 2H7a2 2 0 0 1-2-2V3a2 2 0 0 1 2-2zm0 3v14h10V4z"/></svg>555 389 1642</li>
      <li><svg viewBox="0 0 24 24"><path d="M6 2h12v6H6zM3 9h18a1 1 0 0 1 1 1v8h-4v4H6v-4H2v-8a1 1 0 0 1 1-1zm5 7v4h8v-4z"/></svg>555 902 4418</li>
      <li><svg viewBox="0 0 24 24"><path d="M2 5h20v14H2zm2 2v.5l8 5 8-5V7z"/></svg>dana@clinivo.com</li>
      <li><svg viewBox="0 0 24 24"><circle cx="12" cy="12" r="10"/></svg>www.clinivo.com</li>
    </ul>
    <div class="person"><div class="who">DANA REYES</div><div class="role">CEO/Founder</div></div>
    <div class="tab"></div>
  </section>
</main>
</body>
</html>
```